6"x9" Postcard Mailer

A 6"x9" Postcard mailer targeted to forensic laboratories to advertise or mock forensic samples (https://veltrasync.example/products/mock-forensic-samples/).

Here is some copy, but we can modify if there is not enough space:

Headline:
Expedite Training, Validation, & R&D with Our Ready-to-Use Mock Samples

Bullet Points:

- Wide Variety of Sample Types: IRB-approved samples mimicking crime scene substances, including semen, hair, bone, saliva, blood, and vaginal epithelial cells.
- Diverse Scenarios: Simulate sexual assault and degraded samples for varied conditions.
- Custom Solutions: Tailored DNA quantities and concentrations to suit your lab's needs.

Use discount code PRAX47 for a 10% discount

```html
<!DOCTYPE html>
<html lang="en">
<head>
<meta charset="UTF-8">
<title>Veltrasync Mock Samples Postcard Mailer</title>
<link href="https://fonts.googleapis.com/css2?family=Montserrat:wght@400;500;600;700;800;900&display=swap" rel="stylesheet">
<style>
  :root {
    --navy: #0e2350;
    --navy-deep: #0a1a3e;
    --blue: #1f5fae;
    --sky: #cfe0f2;
    --green: #3fae49;
    --green-dark: #2b8f3a;
    --white: #ffffff;
    --paper: #f4f5f7;
    --ink: #0e2350;
    --muted: #c7d2e6;
  }
  * { box-sizing: border-box; margin: 0; padding: 0; }
  html, body { width: 900px; height: 1200px; overflow: hidden; }
  body {
    background: var(--paper);
    font-family: "Montserrat", Arial, sans-serif;
    position: relative;
  }
  .side-label {
    position: absolute;
    left: 40px;
    width: 60px;
    font-weight: 800;
    font-size: 30px;
    letter-spacing: 4px;
    color: var(--ink);
    transform: rotate(-90deg);
    transform-origin: center;
    text-align: center;
  }
  .side-label--front { top: 245px; }
  .side-label--back { top: 835px; }

  .card {
    position: absolute;
    left: 150px;
    width: 690px;
    height: 460px;
    overflow: hidden;
    box-shadow: 0 6px 18px rgba(10, 26, 62, 0.18);
  }
  .card--front { top: 30px; background: var(--navy); }
  .card--back { top: 620px; background: var(--white); }

  /* Front */
  .hero-photo {
    position: absolute;
    inset: 0 0 170px 0;
    background: linear-gradient(135deg, #eef3f8 0%, #b9cfe6 40%, #2e63b8 70%, #0e2350 100%);
  }
  .headline-band {
    position: absolute;
    left: 0; top: 272px;
    width: 560px; height: 50px;
    background: var(--green);
    clip-path: polygon(0 0, 100% 0, 94% 100%, 0 100%);
    display: flex; align-items: center;
    padding-left: 40px;
  }
  .headline-band h1 {
    font-size: 22px; font-weight: 800; color: var(--white);
    letter-spacing: 0.3px;
  }
  .headline-main {
    position: absolute;
    left: 40px; top: 332px;
    font-size: 33px; font-weight: 800; color: var(--white);
    letter-spacing: 0.3px;
  }
  .front-brand {
    position: absolute;
    right: 40px; bottom: 38px;
    text-align: left;
  }
  .front-brand .brand-name {
    display: flex; align-items: center; gap: 10px;
    font-size: 28px; font-weight: 600; color: var(--white);
  }
  .brand-dot {
    width: 14px; height: 14px; border-radius: 50%;
    background: var(--green);
  }
  .front-brand .tagline {
    font-size: 9px; font-weight: 600; letter-spacing: 2px;
    color: var(--green); margin-top: 4px; padding-left: 24px;
  }

  /* Back */
  .back-panel {
    position: absolute;
    left: 0; top: 0;
    width: 440px; height: 460px;
    background: var(--navy);
    padding: 26px 28px 20px 0;
    color: var(--white);
  }
  .back-panel::after {
    content: "";
    position: absolute;
    right: -14px; top: 0;
    width: 14px; height: 100%;
    background: var(--blue);
  }
  .section-tab {
    display: inline-block;
    background: var(--green);
    color: var(--white);
    font-size: 15px; font-weight: 800;
    padding: 6px 22px 6px 28px;
    clip-path: polygon(0 0, 100% 0, 90% 100%, 0 100%);
  }
  .about-copy {
    padding-left: 28px;
    margin-top: 10px;
    font-size: 9.2px; line-height: 1.45;
    color: var(--muted);
  }
  .about-copy p + p { margin-top: 7px; }
  .provide-tab { margin-top: 16px; }
  .provide-list {
    list-style: none;
    padding-left: 28px;
    margin-top: 10px;
  }
  .provide-list li {
    position: relative;
    padding-left: 14px;
    font-size: 9.2px; line-height: 1.4;
    color: var(--muted);
  }
  .provide-list li + li { margin-top: 8px; }
  .provide-list li::before {
    content: "";
    position: absolute; left: 0; top: 4px;
    width: 6px; height: 6px; border-radius: 50%;
    background: var(--green);
  }
  .provide-list strong {
    display: block;
    color: var(--green); font-weight: 700; font-size: 10px;
  }
  .product-photo {
    position: absolute;
    left: 468px; top: 28px;
    width: 180px; height: 135px;
    background: linear-gradient(160deg, #ffffff 0%, #dfe5ee 55%, #9fb0c8 100%);
  }
  .discount-badge {
    position: absolute;
    left: 478px; top: 220px;
    width: 118px; height: 160px;
    background: var(--green);
    padding: 10px;
    color: var(--white);
    text-align: center;
  }
  .discount-badge .inner {
    border: 2px solid var(--white);
    height: 100%;
    display: flex; flex-direction: column; align-items: center; justify-content: center;
  }
  .discount-badge .label { font-size: 9px; font-weight: 700; letter-spacing: 1.5px; }
  .discount-badge .amount { font-size: 40px; font-weight: 900; line-height: 1; margin-top: 4px; }
  .discount-badge .amount sup { font-size: 16px; }
  .discount-badge .off { font-size: 14px; font-weight: 800; }
  .discount-badge .code-label { font-size: 8px; font-weight: 600; margin-top: 8px; }
  .discount-badge .code { font-size: 14px; font-weight: 800; letter-spacing: 1px; }
  .back-url {
    position: absolute;
    left: 28px; bottom: 10px;
    font-size: 7.5px; color: var(--green);
  }
</style>
</head>
<body>
  <div class="side-label side-label--front">FRONT</div>
  <div class="side-label side-label--back">BACK</div>

  <section class="card card--front">
    <div class="hero-photo" role="img" aria-label="Gloved hands holding a forensic swab and sample tube in a blue-lit laboratory"></div>
    <div class="headline-band">
      <h1>EXPEDITE TRAINING, VALIDATION &amp; R&amp;D</h1>
    </div>
    <h2 class="headline-main">WITH OUR READY-TO-USE MOCK SAMPLES</h2>
    <div class="front-brand">
      <div class="brand-name"><span class="brand-dot"></span>Veltrasync</div>
      <div class="tagline">PRECISION IN EVERY SAMPLE</div>
    </div>
  </section>

  <section class="card card--back">
    <div class="back-panel">
      <div class="section-tab">About Us</div>
      <div class="about-copy">
        <p>Veltrasync Technologies is dedicated to the development of innovative genetic testing solutions that solve crimes and save lives. Here at Veltrasync we strive to provide each lab the necessary samples to ensure that the client's needs are met. Whether that be an off-the-shelf type sample or customizable samples, we can provide you the samples, QC documentation and confidence that the samples we provide will meet your expectations.</p>
        <p>In addition to training and validation, these samples are ideal for competency testing, R&amp;D studies and can be customizable to suit your laboratory's specific needs.</p>
      </div>
      <div class="section-tab provide-tab">We Provide</div>
      <ul class="provide-list">
        <li><strong>Wide Variety of Sample Types:</strong>IRB-approved samples mimicking crime scene substances, including semen, hair, bone, saliva, blood, and vaginal epithelial cells.</li>
        <li><strong>Diverse Scenarios:</strong>Simulate sexual assault and degraded samples for varied conditions.</li>
        <li><strong>Custom Solutions:</strong>Tailored DNA quantities and concentrations to suit your lab's needs.</li>
      </ul>
      <div class="back-url">https://veltrasync.example/products/mock-forensic-samples/</div>
    </div>
    <div class="product-photo" role="img" aria-label="Mock sample kit box with swabs and tubes"></div>
    <div class="discount-badge">
      <div class="inner">
        <div class="label">DISCOUNT</div>
        <div class="amount">10<sup>%</sup></div>
        <div class="off">OFF</div>
        <div class="code-label">USE CODE</div>
        <div class="code">PRAX47</div>
      </div>
    </div>
  </section>
</body>
</html>
```